Benefit Porter

Need home page design for new website. The winner will have the opportunity to design the entire site.

I have attached 3 files.

1) Sort of a site map. PLEASE do not design the home page based on this wire frame. Be creative and use your expertise.

2) Tagline and Copy for the home page. Please just greek in or make up copy for areas that do not have copy at this time.

3) The logo.
Updates

Hi everyone, I am sorry for the delay. I have been out of town on unexpected business. I will make a decision this week. Thank you all for the great designs. Dale

```html
<!DOCTYPE html>
<html lang="en">
<head>
<meta charset="utf-8">
<title>Benefit Porter – Home</title>
<link href="https://fonts.googleapis.com/css2?family=Lato:ital,wght@0,400;0,700;1,400&family=Raleway:wght@500;600&display=swap" rel="stylesheet">
<style>
:root{
  --green:#3aa84a;
  --green-bar:#41ad48;
  --blue:#1d6d95;
  --blue-dark:#175a7c;
  --text:#444;
  --muted:#555;
  --footer:#2b2b2b;
  --footer-line:#555;
  --footer-text:#d8d8d8;
  --light:#f4f4f4;
}
*{box-sizing:border-box;margin:0;padding:0}
html,body{width:914px;height:1200px;overflow:hidden}
body{font-family:"Lato",sans-serif;color:var(--text);background:#fff;position:relative}
.abs{position:absolute}

/* header */
.header{position:absolute;left:0;top:0;width:914px;height:82px;background:linear-gradient(#fff,#ececec)}
.brand{position:absolute;left:104px;top:20px;display:flex;align-items:center;gap:9px}
.brand-dot{width:22px;height:22px;border-radius:50%;background:var(--blue)}
.brand-name{font-family:"Lato",sans-serif;font-size:22px;font-weight:400;color:var(--green)}
.call{position:absolute;left:680px;top:8px;display:flex;gap:8px;align-items:center}
.call-label{font-size:9px;font-weight:700;color:var(--green);letter-spacing:.2px}
.call-num{font-size:15px;font-weight:700;color:var(--blue);line-height:1}
.nav{position:absolute;right:107px;top:56px;display:flex;gap:21px;font-size:10.5px;font-weight:700;color:#333}
.nav .active{color:var(--green);position:relative}
.nav .active::before{content:"";position:absolute;left:50%;top:-16px;width:14px;height:9px;margin-left:-7px;border-radius:50%;background:var(--blue)}

/* hero */
.hero{position:absolute;left:0;top:82px;width:914px;height:372px;background:linear-gradient(#4d7a3a 0%,#5b9a3e 28%,#56a33c 60%,#4c9433 100%)}

/* features */
.features{position:absolute;left:0;top:454px;width:914px;height:292px;background:linear-gradient(#eee,#fff 60%)}
.feature{position:absolute;top:42px;width:240px;text-align:center}
.feature-icon{width:106px;height:106px;border-radius:50%;background:var(--blue);margin:0 auto;display:flex;align-items:center;justify-content:center}
.feature-title{font-family:"Raleway",sans-serif;font-weight:600;font-size:15px;color:var(--green);margin-top:20px}
.feature-text{font-size:11px;line-height:16px;color:var(--muted);margin-top:3px}
.read-more{display:block;margin-top:13px;font-size:10px;font-weight:700;color:var(--blue)}
.divider{position:absolute;top:50px;width:1px;height:200px;background:linear-gradient(transparent,#ddd,transparent)}

/* info band */
.info{position:absolute;left:0;top:746px;width:914px;height:249px;background:#ececec}
.section-head{position:absolute;top:22px;display:flex;align-items:center;gap:10px;font-family:"Raleway",sans-serif;font-weight:600;font-size:16px;color:var(--blue);padding-bottom:12px;border-bottom:1px dashed #c8c8c8}
.section-head span{color:var(--green)}
.quote{position:absolute;left:108px;top:62px;width:328px;height:112px;background:#f8f8f8;border-radius:6px;padding:12px 14px;font-size:10.2px;line-height:17px;font-style:italic;color:#444}
.quote::after{content:"";position:absolute;left:230px;bottom:-20px;border-left:30px solid transparent;border-top:20px solid #f8f8f8}
.quote-mark{font-size:26px;color:#ccc;font-family:Georgia,serif;position:absolute;left:18px;top:4px}
.avatar{position:absolute;left:125px;top:163px;width:58px;height:58px;border-radius:50%;background:linear-gradient(#d9b38f,#b6805a);border:3px solid #fff;box-shadow:0 1px 4px rgba(0,0,0,.3)}
.client-name{position:absolute;left:229px;top:194px;font-size:11px;font-weight:700;color:#333}
.event{position:absolute;left:478px;width:330px;height:62px;border-bottom:1px dashed #c8c8c8}
.date{position:absolute;left:1px;top:0;width:32px;height:37px;background:var(--blue);color:#fff;text-align:center;font-weight:700}
.date b{display:block;font-size:14px;line-height:18px;padding-top:2px}
.date i{display:block;font-style:normal;font-size:9px;background:var(--blue-dark);line-height:15px}
.date::after{content:"";position:absolute;right:-5px;top:6px;border-left:5px solid var(--blue);border-top:5px solid transparent;border-bottom:5px solid transparent}
.event-title{position:absolute;left:50px;top:-3px;font-size:11px;font-weight:700;color:var(--blue)}
.event-text{position:absolute;left:50px;top:12px;width:282px;font-size:9.5px;line-height:14px;color:#444}

/* footer */
.footer{position:absolute;left:0;top:995px;width:914px;height:178px;background:var(--footer);color:var(--footer-text)}
.f-col{position:absolute;top:20px}
.f-head{font-size:14px;color:#fff;padding-bottom:6px;border-bottom:1px solid var(--footer-line);margin-bottom:10px}
.f-links{list-style:none;font-size:10px}
.f-links li{height:18.4px}
.f-links li::before{content:"›";margin-right:7px}
.f-row{display:flex;gap:10px;font-size:10px;line-height:13px;margin-bottom:12px}
.map{width:166px;height:84px;background:linear-gradient(135deg,#dfe5d5,#bcd3ea 55%,#e9d9b0);border:2px solid #fff}
.view{font-size:9.5px;margin-top:7px;display:block}
.social{display:flex;align-items:center;gap:9px;font-size:10px;height:24px}
.social i{width:16px;height:16px;background:#fff;display:block}
.copyright{position:absolute;left:0;top:1173px;width:914px;height:27px;background:var(--green-bar);color:#fff;font-size:10px;text-align:center;line-height:27px}
</style>
</head>
<body>

<header class="header">
  <div class="brand"><span class="brand-dot"></span><span class="brand-name">BenefitPorter.com</span></div>
  <div class="call">
    <svg width="28" height="28" viewBox="0 0 28 28"><circle cx="14" cy="14" r="12.5" fill="none" stroke="var(--green)" stroke-width="2"/><path d="M10 8c1-1 2 0 3 2s0 2-1 3c1 2 2 3 4 4 1-1 1-2 3-1s3 2 2 3c-1 2-3 2-5 1-3-2-5-4-7-7-1-2-1-4 1-5z" fill="var(--green)"/></svg>
    <div><div class="call-label">CALL US TODAY</div><div class="call-num">555-014-2290</div></div>
  </div>
  <nav class="nav"><span class="active">PRICING</span><span>FEATURES</span><span>SERVICES</span><span>PRODUCTS</span><span>ABOUT</span><span>CONTACT</span></nav>
</header>

<section class="hero" role="img" aria-label="Photo of golfers putting on a green at a charity tournament, sponsor banners behind"></section>

<section class="features">
  <div class="feature" style="left:87px">
    <div class="feature-icon"><svg width="56" height="50" viewBox="0 0 56 50" fill="#fff"><rect x="2" y="30" width="6" height="18"/><rect x="11" y="24" width="6" height="24"/><rect x="20" y="18" width="6" height="30"/><path d="M6 24 34 8l-3-5 14 0-6 12-3-5L8 28z"/><circle cx="44" cy="38" r="9" fill="none" stroke="#fff" stroke-width="3"/></svg></div>
    <div class="feature-title">Raise More, Stress Less</div>
    <p class="feature-text">Lorem ipsum dolor sit amet consetug e sed diay nibh euismodl tincidunt ut laoreet dolore magam er vol wisi enim ad</p>
    <span class="read-more">READ MORE »</span>
  </div>
  <div class="divider" style="left:333px"></div>
  <div class="feature" style="left:336px">
    <div class="feature-icon"><svg width="60" height="38" viewBox="0 0 60 38"><rect x="2" y="2" width="48" height="34" rx="6" fill="#fff"/><rect x="8" y="13" width="14" height="4" fill="var(--blue)"/><rect x="8" y="20" width="8" height="3" fill="var(--blue)"/><circle cx="46" cy="22" r="12" fill="var(--blue)"/><path d="M40 22l5 5 9-11" fill="none" stroke="#fff" stroke-width="3.5"/></svg></div>
    <div class="feature-title">Everything You Need</div>
    <p class="feature-text">Lorem ipsum dolor sit amet consetug e sed diay nibh euismodl tincidunt ut laoreet dolore magam er vol wisi enim ad</p>
    <span class="read-more">READ MORE »</span>
  </div>
  <div class="divider" style="left:579px"></div>
  <div class="feature" style="left:586px">
    <div class="feature-icon"><svg width="60" height="46" viewBox="0 0 60 46" fill="#fff"><rect x="20" y="4" width="14" height="20" rx="2" transform="rotate(-40 27 14)"/><rect x="30" y="16" width="24" height="5" transform="rotate(35 30 18)"/><rect x="6" y="30" width="32" height="5"/><rect x="2" y="38" width="40" height="6"/></svg></div>
    <div class="feature-title">Sold! Silent Auction Moducle</div>
    <p class="feature-text">Lorem ipsum dolor sit amet consetug e sed diay nibh euismodl tincidunt ut laoreet dolore magam er vol wisi enim ad</p>
    <span class="read-more">READ MORE »</span>
  </div>
</section>

<section class="info">
  <h2 class="section-head" style="left:105px;width:330px">
    <svg width="19" height="17" viewBox="0 0 19 17" fill="#2b2b2b"><path d="M1 1h11v8H6l-3 3V9H1z"/><path d="M13 5h5v8h-2v3l-3-3H8v-3h5z"/></svg>
    Client <span>Testimonials</span></h2>
  <div class="quote"><span class="quote-mark">“</span><p style="text-indent:28px">Lorem ipsum dolor sit amet consetug e sed diay nibh euismodl tincidunt ut laoreet dolore magam er vol wisi enim ad minim veniam quis nostrud exerci tationorem ipsum dolor sit ametee sed diammmy nibh euismd tincidunt ut laoreet dolore magna aliqur volpatl tiidunt ut laoreet dolore magna aliqur volpatl</p></div>
  <div class="avatar" role="img" aria-label="Portrait photo of the client"></div>
  <div class="client-name">Mr.Owen Hartley</div>

  <h2 class="section-head" style="left:479px;width:328px">
    <svg width="19" height="19" viewBox="0 0 19 19" fill="none" stroke="#2b2b2b" stroke-width="2"><rect x="1" y="3" width="17" height="15"/><path d="M1 7h17M5 1v4M14 1v4M5 11h2M9 11h2M13 11h2M5 14h2M9 14h2"/></svg>
    Seminars <span>and</span> Events</h2>
  <div class="event" style="top:62px"><div class="date"><b>29</b><i>FEB</i></div><div class="event-title">Duis autem vel eumsodn</div><p class="event-text">Lorem ipsum dolor sit ametm nk consectetuer adipiscing elremo ipsum dolor sit ametm nk consectetuer.</p></div>
  <div class="event" style="top:124px"><div class="date"><b>29</b><i>FEB</i></div><div class="event-title">Bibh euismodl tincidunt ut laoreet dolore magam</div><p class="event-text">Lorem ipsum dolor sit ametm nk consectetuer adipiscing loremo ipsum dolor sit ametm nk consectetuer.</p></div>
  <div class="event" style="top:186px;border:0"><div class="date"><b>29</b><i>FEB</i></div><div class="event-title">Samet consetug e sed diay nibh euismodl</div><p class="event-text">Lorem ipsum dolor sit ametm nk consectetuer adipiscing elremo ipsum dolor sit ametm nk consectetuer.</p></div>
</section>

<footer class="footer">
  <div class="f-col" style="left:106px;width:93px">
    <div class="f-head">Quick Links</div>
    <ul class="f-links"><li>Pricing</li><li>Features</li><li>Services</li><li>Products</li><li>About</li><li>Contact</li></ul>
  </div>
  <div class="f-col" style="left:251px;width:178px">
    <div class="f-head">Contact Information</div>
    <div class="f-row"><svg width="9" height="12" viewBox="0 0 9 12"><path d="M4.5 0a4.5 4.5 0 0 1 4.5 4.5C9 8 4.5 12 4.5 12S0 8 0 4.5A4.5 4.5 0 0 1 4.5 0z" fill="#fff"/><circle cx="4.5" cy="4.5" r="1.7" fill="var(--footer)"/></svg><span>Lorem ipsum dolor sit consectetuer adipiscing elit, diam nonummy nibh Street No 5, zip Code: 897410</span></div>
    <div class="f-row"><svg width="10" height="10" viewBox="0 0 10 10"><path d="M2 0c1 0 2 2 2 3L3 4c1 1 2 2 3 3l1-1c1 0 3 1 3 2s-1 2-2 2C4 10 0 6 0 2 0 1 1 0 2 0z" fill="#fff"/></svg><span>555-014-2290</span></div>
    <div class="f-row"><svg width="11" height="8" viewBox="0 0 11 8"><rect width="11" height="8" fill="#fff"/><path d="M0 0l5.5 4.5L11 0" stroke="var(--footer)" fill="none"/></svg><span>hello@benefitporter.com</span></div>
  </div>
  <div class="f-col" style="left:483px;width:166px">
    <div class="f-head">Location Map</div>
    <div class="map" role="img" aria-label="Street map showing the office location"></div>
    <span class="view">View Location »</span>
  </div>
  <div class="f-col" style="left:701px;width:93px">
    <div class="f-head">Follow Us</div>
    <div class="social"><i></i>Circlepage</div>
    <div class="social"><i></i>Chirpline</div>
    <div class="social"><i></i>Orbitnet</div>
    <div class="social"><i></i>Workweb</div>
  </div>
</footer>
<div class="copyright">© 2014 BenefitPorter &nbsp;|&nbsp; All rights reserved</div>

</body>
</html>
```